Create a wine label for our soon to be released Sparkling Wine

As we are about to release our new Sparkling Wine we are in need of a new label. Dimensions and text as per attached file, the design is more or less free style, but keep it a classic sparkling wine label. Keep it clean. Bottle will be near to black with black/silver cap You can use Script Font. No green, red or gold colours. We like black and silver, but don't be afraid to use some color somewhere (we can always change that). We thought of printing our logo in silver foil so a black label would be nice.

Target Market(s)

wine industry

Font styles to use
Script
Other font styles liked:
• GaramITC

Requirements
Must have
• Dimensions and text as per attached file
Nice to have
• Classic wine label
Should not have
• No gold or red or green colour

```html
<!DOCTYPE html>
<html lang="en">
<head>
<meta charset="UTF-8">
<title>Frost Hollow – Blanc de Noir Label</title>
<link href="https://fonts.googleapis.com/css2?family=Cinzel:wght@400;700&family=Pinyon+Script&display=swap" rel="stylesheet">
<style>
  :root {
    --backdrop-light: #8a8583;
    --backdrop-dark: #4e4a49;
    --label-black: #141414;
    --stripe-grey: #2a2a2a;
    --frame-silver: #e4e2e8;
    --frame-lavender: #9c88c8;
    --wordmark-silver: #e8e8ea;
    --script-grey: #b9b9bd;
    --varietal-purple: #9a82d0;
    --detail-silver: #cfcfd3;
    --scene-haze: rgba(120, 120, 124, 0.22);
    --scene-haze-soft: rgba(90, 90, 94, 0.10);
  }
  html, body {
    margin: 0;
    padding: 0;
    width: 1200px;
    height: 800px;
    overflow: hidden;
  }
  body {
    background: radial-gradient(ellipse at 50% 40%, var(--backdrop-light), var(--backdrop-dark));
    font-family: "Cinzel", Georgia, serif;
  }
  .wine-label {
    position: absolute;
    left: 300px;
    top: 140px;
    width: 600px;
    height: 520px;
  }
  .label-frame {
    position: absolute;
    inset: 0;
  }
  .wordmark {
    position: absolute;
    top: 50px;
    left: 0;
    right: 0;
    text-align: center;
    font-size: 60px;
    font-weight: 400;
    letter-spacing: 1px;
    color: var(--wordmark-silver);
    margin: 0;
    line-height: 1;
  }
  .region {
    position: absolute;
    top: 118px;
    left: 160px;
    font-family: "Pinyon Script", cursive;
    font-size: 30px;
    color: var(--script-grey);
    margin: 0;
  }
  .landscape-art {
    position: absolute;
    top: 160px;
    left: 40px;
    width: 520px;
    height: 190px;
    background:
      radial-gradient(ellipse 45% 40% at 62% 62%, var(--scene-haze), transparent 100%),
      radial-gradient(ellipse 30% 55% at 18% 55%, var(--scene-haze-soft), transparent 100%);
  }
  .varietal {
    position: absolute;
    top: 365px;
    left: 0;
    right: 0;
    text-align: center;
    font-size: 30px;
    font-weight: 700;
    color: var(--varietal-purple);
    margin: 0;
  }
  .details {
    position: absolute;
    top: 412px;
    left: 90px;
    display: grid;
    grid-template-columns: auto auto;
    column-gap: 16px;
    row-gap: 2px;
    font-size: 16px;
    color: var(--detail-silver);
    margin: 0;
  }
  .details dt { text-align: right; margin: 0; }
  .details dd { margin: 0; }
</style>
</head>
<body>
  <main class="wine-label">
    <svg class="label-frame" width="600" height="520" viewBox="0 0 600 520" aria-hidden="true">
      <defs>
        <pattern id="pinstripe" width="12" height="10" patternUnits="userSpaceOnUse">
          <rect width="12" height="10" fill="var(--label-black)"/>
          <rect x="0" width="5" height="10" fill="var(--stripe-grey)"/>
        </pattern>
      </defs>
      <path fill="var(--frame-silver)"
        d="M18,0 H582 A18 18 0 0 0 600 18 V502 A18 18 0 0 0 582 520 H18 A18 18 0 0 0 0 502 V18 A18 18 0 0 0 18 0 Z"/>
      <path fill="var(--frame-lavender)"
        d="M20.8,3 H579.2 A21 21 0 0 0 597 20.8 V499.2 A21 21 0 0 0 579.2 517 H20.8 A21 21 0 0 0 3 499.2 V20.8 A21 21 0 0 0 20.8 3 Z"/>
      <path fill="url(#pinstripe)"
        d="M26.2,10 H573.8 A28 28 0 0 0 590 26.2 V493.8 A28 28 0 0 0 573.8 510 H26.2 A28 28 0 0 0 10 493.8 V26.2 A28 28 0 0 0 26.2 10 Z"/>
    </svg>

    <h1 class="wordmark">Frost Hollow</h1>
    <p class="region">Tasmania</p>

    <div class="landscape-art" role="img" aria-label="Faint line illustration of a bare tree, rolling mountains and a winding brook"></div>

    <h2 class="varietal">Blanc de Noir</h2>

    <dl class="details">
      <dt>Product of Australia</dt><dd>2013</dd>
      <dt>750ml</dt><dd>Vintage Sparkling</dd>
      <dt>Alc/Vol 12.5%</dt><dd>Méthode Traditionnelle</dd>
    </dl>
  </main>
</body>
</html>
```